Hurricane Damage Public Adjuster Billboard

I have created several projects with you and have several great designs. I need to format them into a Billboard for upcoming Hurricane Season. Need done in a month. Im also in process of getting an eye catching and easy to remember 800# Vanity phone number like Call 800-Stormsafe or 800- Need Help? My included past Pixel Bazaar projects will give you an idea of what colors, schemes, and designs I gravitate towards. 3 past Design projects were 1) 2 Logos where I picked the 1st place and the 2nd place and 2) Index Card where I picked the winner as the Index Card and the 2nd place as a Post Card. Point is, I will pick and pay for 2 winners if they're good. This should help to sweeten the pot. Also, please look at my website for ideas that I like:

www.CedarlineClaimHelp.com
I want people to feel that I am the best and highest. Level.

I've been getting a lot of quick half effort designs basically cut & pasting my previous projects. Please don't rush and take your time to be creative. A an example, my Biggest Competitor is Tamarack Public Adjusting. Their colors are Black and Gold while mine are Blue, White, and Black with a highlight of Orange if possible. I JUST imported a picture of their BillBoard. I need mine better and BLOW AWAY THEIRS. Terms like "Don't be Victimized Twice ?, Don't let the Hurricane Ruin your Life?". "Get Fairly Paid & Move On" "Our Clients Claims are VIP?
Updates

I'm getting a lot of quick half effort ones. I'd rather you take your time and really put some thoughts and effort into it. My Biggest Competitor is Tamarack Public Adjusting. They have black & gold colors, while I have Blue, Black, and white.

It needs to blow theirs away. I have imported their Billboard for comparative purposes.

Guy's,
I'll make it easier for you in what I'm looking for. Please look at the Tamarack Billboard picture attached.

1) Put my "Blue Shield" to the left, replacing their logo
2) change color patterns from their (Black, Gold, White) to my color schemes of (Black, Blue, White)
3) I want to see my name where their is:

THE
Cedarline Claim Help
EXPERT & LOCAL Public Adjusters
"FOR THE POLICYHOLDER!!"

4) to the right, add the A+Rated logo and QRT+ Accredited logo, 5 Star Zorvex Rated logo, 5 Start PORCHLINK Highly Rated logo, etc..

5) the right side is where you can be creative as I will not have a picture of me there.

"20+ Years of Experience, Recovering Millions for our VIP Clients"

"Your Best, Locally-Based Private Adjuster & Advocate'
"FOR THE POLICYHOLDER!!"

"Don't be victimized Twice!!"

"Don't let the Hurricane Ruin Your Life!!"

This should really help. Also, refer to my website, maybe a couple testimonial fillers?

Thanks all,

marcus@CedarlineClaimHelp.com

Just imported a few awards that would look great to the right side with all the other 5 Star Ratings and accolades.
This right section could be titled like zmy Website:

5 Star Reviews, Ratings & Awards:
4-5 Logos underneath?

Target Market(s)

Coastal place where a Hurricane 🌀 🌀 Hits

Industry/Entity Type

Hurricane Public Insurance Adjuster

Font styles to use
Sans Serif
Other font styles liked:
• Zurich fonts

Colors
0054AA
0677BA
7BADD7
CADEEF
E8F1F8
EE7325
F08F49
F5BC92
FAE3D3
FDF4ED

Requirements
Must have
• Use my past project logos, colors, and schemes to create eye grabbing BillBoard
Nice to have
Should not have
• Not be too busy, must be Easy to Read, Eye Catchy

```html
<!DOCTYPE html>
<html lang="en">
<head>
<meta charset="utf-8">
<title>Cedarline Claim Help – Hurricane Season Billboard</title>
<link rel="stylesheet" href="https://fonts.googleapis.com/css2?family=Montserrat:ital,wght@0,400;0,500;0,700;0,800;1,500&family=Crimson+Pro:wght@500;600&display=swap">
<style>
  :root {
    --page: #d9d9d9;
    --ink-dark: #151d21;
    --ink-mid: #1d2a30;
    --blue: #1f8fdc;
    --blue-light: #35a9f0;
    --blue-deep: #0054aa;
    --white: #ffffff;
    --grey-text: #c8ced2;
    --orange: #ee7325;
    --gold-star: #f6b81c;
    --porch-green: #6cc04a;
  }
  * { box-sizing: border-box; margin: 0; padding: 0; }
  html, body { width: 998px; height: 1200px; overflow: hidden; }
  body { background: var(--page); font-family: "Montserrat", sans-serif; position: relative; }

  .billboard {
    position: absolute; left: 29px; top: 365px;
    width: 940px; height: 470px; overflow: hidden;
    background: linear-gradient(160deg, var(--ink-mid), var(--ink-dark) 60%);
    box-shadow: 0 6px 16px rgba(0,0,0,.35);
  }
  .billboard__storm { position: absolute; inset: 0; }

  .brand__mark { position: absolute; left: 40px; top: 30px; width: 50px; height: 50px; background: var(--blue-light); }
  .brand { position: absolute; left: 113px; top: 24px; }
  .brand__name {
    font-family: "Crimson Pro", serif; font-weight: 500; font-size: 22px; line-height: 23px;
    color: var(--blue-light); letter-spacing: .5px; text-transform: uppercase;
  }
  .brand__tagline { margin-top: 6px; font-size: 12.5px; color: var(--grey-text); letter-spacing: .3px; }
  .brand__slogan { font-size: 10px; font-style: italic; font-weight: 500; color: var(--blue-light); letter-spacing: 3.6px; margin-top: 2px; }

  .headline {
    position: absolute; left: 30px; top: 132px;
    font-family: "Crimson Pro", serif; font-weight: 600; font-size: 28px; line-height: 31px;
    color: var(--blue-light); text-transform: uppercase; letter-spacing: -.2px;
  }
  .subhead { position: absolute; left: 30px; top: 204px; font-size: 19.5px; font-style: italic; font-weight: 500; color: var(--white); }
  .warning {
    position: absolute; left: 27px; top: 236px;
    font-family: "Crimson Pro", serif; font-weight: 500; font-size: 21px; color: var(--orange); text-transform: uppercase;
  }

  .experience { position: absolute; left: 24px; top: 277px; width: 136px; text-align: center; }
  .experience__badge {
    display: block; margin: 0 auto; width: 128px; height: 136px; border-radius: 10px 10px 50% 50%;
    background: radial-gradient(circle at 50% 40%, #2a3640 38%, #1f8fdc 40%, #35a9f0 70%, #1a6fae);
  }
  .experience__caption { font-family: "Crimson Pro", serif; font-size: 13px; line-height: 13px; color: var(--blue-light); margin-top: 9px; }

  .divider { position: absolute; left: 183px; top: 277px; width: 2px; height: 168px; background: var(--white); opacity: .85; }

  .services { position: absolute; left: 206px; top: 275px; list-style: none; }
  .services__item { display: flex; align-items: center; gap: 8px; height: 27.8px; font-size: 15px; color: var(--white); }

  .call { position: absolute; left: 515px; top: 18px; font-size: 35px; line-height: 42px; font-weight: 700; color: var(--white); }
  .contact { position: absolute; left: 520px; top: 108px; }
  .contact__row { display: flex; align-items: center; gap: 10px; height: 35px; font-size: 16.5px; font-weight: 700; color: var(--white); text-transform: uppercase; letter-spacing: .1px; }
  .contact__icon { width: 30px; height: 30px; border-radius: 50%; background: var(--white); display: flex; align-items: center; justify-content: center; flex: none; }

  .storm-photo {
    position: absolute; width: 168px; height: 168px; border-radius: 50%;
    border: 5px solid var(--white); top: 203px;
  }
  .storm-photo--city { left: 570px; background: radial-gradient(circle at 55% 45%, #c7d3f2, #3a63c6 40%, #1a2a63 75%, #0b1224); }
  .storm-photo--bolts { left: 748px; background: radial-gradient(circle at 50% 40%, #79d4e6, #256a8e 45%, #0d2636 80%); }

  .ratings__accredited { position: absolute; left: 623px; top: 389px; width: 98px; height: 36px; border-radius: 4px; background: var(--blue-deep); border: 2px solid var(--white); }
  .ratings__review { position: absolute; text-align: center; }
  .ratings__review--zorvex { left: 740px; top: 388px; width: 100px; }
  .ratings__review--porch { left: 842px; top: 402px; width: 88px; }
  .ratings__name { font-size: 20px; font-weight: 700; color: var(--white); line-height: 22px; }
  .ratings__name--porch { font-size: 12.5px; line-height: 15px; color: var(--porch-green); }
  .stars { display: flex; gap: 2px; justify-content: center; margin-top: 3px; }
</style>
</head>
<body>
  <section class="billboard" aria-label="Cedarline Claim Help hurricane season billboard">
    <svg class="billboard__storm" width="940" height="470" viewBox="0 0 940 470">
      <defs>
        <linearGradient id="storm-sky" x1="0" y1="0" x2="1" y2="1">
          <stop offset="0" stop-color="#1b3a41"/>
          <stop offset=".45" stop-color="#2b6268"/>
          <stop offset="1" stop-color="#0f2328"/>
        </linearGradient>
      </defs>
      <path role="img" aria-label="Dark stormy sky with lightning over the sea"
            d="M462 0 H940 V470 H634 Q470 300 462 0 Z" fill="url(#storm-sky)"/>
      <path d="M450 0 Q458 300 624 470" fill="none" stroke="var(--blue)" stroke-width="10"/>
    </svg>

    <span class="brand__mark"></span>
    <header class="brand">
      <p class="brand__name">The Cedarline<br>Claim Help</p>
      <p class="brand__tagline">EXPERT &amp; LOCAL PUBLIC ADJUSTERS</p>
      <p class="brand__slogan">FOR THE POLICYHOLDER!!</p>
    </header>

    <h1 class="headline">Your best, locally-based<br>private adjuster &amp; advocate</h1>
    <p class="subhead">FOR THE POLICYHOLDER!!</p>
    <p class="warning">Don't let the hurricane ruin your life!!</p>

    <div class="experience">
      <div class="experience__badge" role="img" aria-label="Blue shield badge with ribbons reading 20 years of experience"></div>
      <p class="experience__caption">Recovering Millions<br>for our VIP Clients</p>
    </div>

    <div class="divider"></div>

    <ul class="services">
      <li class="services__item"><svg width="12" height="14" viewBox="0 0 12 14"><path d="M6 1 L11 3 Q11 10 6 13 Q1 10 1 3 Z" fill="none" stroke="var(--blue-light)" stroke-width="1.3"/><path d="M3.5 7 L5.5 9 L8.5 5" fill="none" stroke="var(--blue-light)" stroke-width="1.3"/></svg>Residential Claims</li>
      <li class="services__item"><svg width="12" height="14" viewBox="0 0 12 14"><path d="M6 1 L11 3 Q11 10 6 13 Q1 10 1 3 Z" fill="none" stroke="var(--blue-light)" stroke-width="1.3"/><path d="M3.5 7 L5.5 9 L8.5 5" fill="none" stroke="var(--blue-light)" stroke-width="1.3"/></svg>Commercial Claims</li>
      <li class="services__item"><svg width="12" height="14" viewBox="0 0 12 14"><path d="M6 1 L11 3 Q11 10 6 13 Q1 10 1 3 Z" fill="none" stroke="var(--blue-light)" stroke-width="1.3"/><path d="M3.5 7 L5.5 9 L8.5 5" fill="none" stroke="var(--blue-light)" stroke-width="1.3"/></svg>Insurance Appraisals</li>
      <li class="services__item"><svg width="12" height="14" viewBox="0 0 12 14"><path d="M6 1 L11 3 Q11 10 6 13 Q1 10 1 3 Z" fill="none" stroke="var(--blue-light)" stroke-width="1.3"/><path d="M3.5 7 L5.5 9 L8.5 5" fill="none" stroke="var(--blue-light)" stroke-width="1.3"/></svg>Contractor Evaluation &amp; Vetting</li>
      <li class="services__item"><svg width="12" height="14" viewBox="0 0 12 14"><path d="M6 1 L11 3 Q11 10 6 13 Q1 10 1 3 Z" fill="none" stroke="var(--blue-light)" stroke-width="1.3"/><path d="M3.5 7 L5.5 9 L8.5 5" fill="none" stroke="var(--blue-light)" stroke-width="1.3"/></svg>Construction Consulting</li>
      <li class="services__item"><svg width="12" height="14" viewBox="0 0 12 14"><path d="M6 1 L11 3 Q11 10 6 13 Q1 10 1 3 Z" fill="none" stroke="var(--blue-light)" stroke-width="1.3"/><path d="M3.5 7 L5.5 9 L8.5 5" fill="none" stroke="var(--blue-light)" stroke-width="1.3"/></svg>Home Inspection Services</li>
    </ul>

    <h2 class="call">Call 800-Stormsafe or<br>800- Need Help?</h2>

    <div class="contact">
      <p class="contact__row">
        <span class="contact__icon"><svg width="18" height="18" viewBox="0 0 18 18" fill="none" stroke="var(--blue)" stroke-width="1.4"><circle cx="9" cy="9" r="7.5"/><ellipse cx="9" cy="9" rx="3.5" ry="7.5"/><path d="M1.5 9 H16.5 M3 5 H15 M3 13 H15"/></svg></span>
        www.CedarlineClaimHelp.com
      </p>
      <p class="contact__row">
        <span class="contact__icon"><svg width="18" height="14" viewBox="0 0 18 14" fill="none" stroke="var(--blue)" stroke-width="1.5"><rect x="1" y="1" width="16" height="12" rx="1.5"/><path d="M1 2 L9 8 L17 2"/></svg></span>
        marcus@CedarlineClaimHelp.com
      </p>
    </div>

    <div class="storm-photo storm-photo--city" role="img" aria-label="Photo of lightning striking over a city skyline at night"></div>
    <div class="storm-photo storm-photo--bolts" role="img" aria-label="Photo of branching lightning bolts in a dark storm"></div>

    <div class="ratings__accredited" role="img" aria-label="Accreditation badge"></div>
    <div class="ratings__review ratings__review--zorvex">
      <p class="ratings__name">Zorvex</p>
      <div class="stars">
        <svg width="14" height="14" viewBox="0 0 10 10"><path d="M5 0 L6.2 3.6 L10 3.6 L7 5.9 L8.1 9.5 L5 7.3 L1.9 9.5 L3 5.9 L0 3.6 L3.8 3.6 Z" fill="var(--gold-star)"/></svg>
        <svg width="14" height="14" viewBox="0 0 10 10"><path d="M5 0 L6.2 3.6 L10 3.6 L7 5.9 L8.1 9.5 L5 7.3 L1.9 9.5 L3 5.9 L0 3.6 L3.8 3.6 Z" fill="var(--gold-star)"/></svg>
        <svg width="14" height="14" viewBox="0 0 10 10"><path d="M5 0 L6.2 3.6 L10 3.6 L7 5.9 L8.1 9.5 L5 7.3 L1.9 9.5 L3 5.9 L0 3.6 L3.8 3.6 Z" fill="var(--gold-star)"/></svg>
        <svg width="14" height="14" viewBox="0 0 10 10"><path d="M5 0 L6.2 3.6 L10 3.6 L7 5.9 L8.1 9.5 L5 7.3 L1.9 9.5 L3 5.9 L0 3.6 L3.8 3.6 Z" fill="var(--gold-star)"/></svg>
        <svg width="14" height="14" viewBox="0 0 10 10"><path d="M5 0 L6.2 3.6 L10 3.6 L7 5.9 L8.1 9.5 L5 7.3 L1.9 9.5 L3 5.9 L0 3.6 L3.8 3.6 Z" fill="var(--gold-star)"/></svg>
      </div>
    </div>
    <div class="ratings__review ratings__review--porch">
      <p class="ratings__name ratings__name--porch">PORCHLINK</p>
      <div class="stars">
        <svg width="8" height="8" viewBox="0 0 10 10"><path d="M5 0 L6.2 3.6 L10 3.6 L7 5.9 L8.1 9.5 L5 7.3 L1.9 9.5 L3 5.9 L0 3.6 L3.8 3.6 Z" fill="var(--gold-star)"/></svg>
        <svg width="8" height="8" viewBox="0 0 10 10"><path d="M5 0 L6.2 3.6 L10 3.6 L7 5.9 L8.1 9.5 L5 7.3 L1.9 9.5 L3 5.9 L0 3.6 L3.8 3.6 Z" fill="var(--gold-star)"/></svg>
        <svg width="8" height="8" viewBox="0 0 10 10"><path d="M5 0 L6.2 3.6 L10 3.6 L7 5.9 L8.1 9.5 L5 7.3 L1.9 9.5 L3 5.9 L0 3.6 L3.8 3.6 Z" fill="var(--gold-star)"/></svg>
        <svg width="8" height="8" viewBox="0 0 10 10"><path d="M5 0 L6.2 3.6 L10 3.6 L7 5.9 L8.1 9.5 L5 7.3 L1.9 9.5 L3 5.9 L0 3.6 L3.8 3.6 Z" fill="var(--gold-star)"/></svg>
        <svg width="8" height="8" viewBox="0 0 10 10"><path d="M5 0 L6.2 3.6 L10 3.6 L7 5.9 L8.1 9.5 L5 7.3 L1.9 9.5 L3 5.9 L0 3.6 L3.8 3.6 Z" fill="var(--gold-star)"/></svg>
      </div>
    </div>
  </section>
</body>
</html>
```